wordpress website Clara Wendell, Author, Speaker and Coach

Need a wordpress blogging website for author/speaker/coach.
I have paid for hosting on nestpanda.
I am currently writing a book - Launchpad for Campus - Steps and strategies to prepare you to thrive in college and beyond. Eventually, I will have an Academic/Life Coaching program targeting high school and college students. This website's purpose is to build my email list. I can offer the following reports as incentive for email sign-up:
1. Seven Habits That Carry Your Teen Through University on Schedule and Budget
2. Creative Routes to Fund University
3. SAT/ACT vocabulary word of the day

facebook page: https://www.facebook.com/Clara-Wendell-AcademicLife-Coach-915730284613902/

I would like to have these pages:

1. Home or About page

High school is becoming more and more stressful for students. Not only are they taking more AP classes than ever before, and often spending $1,000’s on SAT/ACT prep programs, most are NOT prepared for success in college. Only 19% of students are graduating from college within 4 years and only 56% are graduating within 6 years. With the cost of higher education skyrocketing, each extra year of school can costs families $40,000 - $60,000 when you factor in living expenses. Then, when students do graduate, they are often underemployed.

Clara's approach is whole person oriented. Her programs help students learn life skills in addition to the study, time management skills, etc. offered by most academic coaching programs. Our program addresses all of the major causes of failure to graduate within 4 years, and is based on sound educational research. Clara's program initially provides the daily interaction needed to successfully change behaviors and seat new success habits, unlike many programs in which students interact with coaches only once a week.
Bio
Clara Wendell is a certified teacher and holds advanced certification in academic coaching and tutoring. She also is a certified trainer in the Hollis Varga Growth Framework. She has three successful adult children, and helped them overcome learning differences and thrive.

2. Blog

3. Contact - Include form (I split time between USA and Saudi Arabia, so I will call or email people back, but don't want to leave a phone number)
info@clarawendell.example

4. Store – 1 book for now
Launchpad for Campus
Steps and strategies to prepare you to thrive in college and beyond
Available 12/01/2017
I could make a preview chapter available for download

5. Speaking
Clara Wendell is available for keynote addresses and half-day, full day or multi-day workshops. I will develop details later

6.Coaching programs
I will develop details later

Target Market(s)

high school students who are college bound and their parents

Number of Pages Required

5+ page

Font styles to use
Sans Serif

Colors

Designer to choose colors to be used in the design.

Requirements
Nice to have
• integration with post finch for contact management

```html
<!DOCTYPE html>
<html lang="en">
<head>
<meta charset="utf-8">
<title>Clara Wendell — Author, Speaker and Coach</title>
<link rel="stylesheet" href="https://fonts.googleapis.com/css2?family=Mulish:wght@400;600;700&family=Open+Sans:wght@400;600&display=swap">
<style>
:root{
  --green:#0f7d3f;
  --green-bright:#3aa64f;
  --green-dark:#0b6a33;
  --purple:#8a82c6;
  --purple-soft:#a39cd6;
  --ink:#333;
  --muted:#777;
  --light:#efefef;
  --white:#fff;
}
*{box-sizing:border-box;margin:0;padding:0}
html,body{width:1200px;height:2922px;overflow:hidden}
body{position:relative;font-family:"Open Sans",sans-serif;color:var(--ink);background:var(--white)}
.abs{position:absolute}

/* header */
.site-header{left:0;top:0;width:1200px;height:92px;background:var(--white)}
.brand{left:128px;top:24px;display:flex;align-items:center;gap:12px}
.brand-dot{width:40px;height:40px;border-radius:50%;background:var(--purple)}
.brand-name{font-family:"Mulish",sans-serif;font-size:34px;color:var(--green);font-weight:400}
.main-nav{top:34px;left:0;width:1200px;font-family:"Mulish",sans-serif;font-size:18px;color:#8a8a8a}
.main-nav a{position:absolute;color:inherit;text-decoration:none;white-space:nowrap}
.main-nav a.active{color:var(--green);font-weight:600}

/* hero */
.hero{left:0;top:92px;width:1200px;height:560px;overflow:hidden}
.hero-photo{left:0;top:0;width:1200px;height:560px;background:linear-gradient(90deg,#34332f 0%,#4a4640 45%,#6b6258 75%,#85786a 100%)}
.hero-title{left:168px;top:200px;font-family:"Mulish",sans-serif;font-size:36px;color:var(--white);letter-spacing:.5px}
.hero-sub{left:168px;top:256px;font-family:"Mulish",sans-serif;font-size:16px;line-height:25px;color:var(--white);text-transform:uppercase}
.btn-solid{left:168px;top:322px;width:120px;height:32px;border-radius:16px;background:var(--green);color:var(--white);font-size:12px;line-height:32px;text-align:center;text-transform:uppercase}
.book{left:705px;top:102px;width:270px;height:350px;background:linear-gradient(180deg,#8a8f86 0%,#6e8a5f 45%,#18883c 62%,#118239 100%);box-shadow:6px 6px 14px rgba(0,0,0,.4)}
.arrow{top:240px}
.hero-wave{left:0;top:440px}

/* bio */
.bio{left:0;top:643px;width:1200px;height:352px;background:var(--light)}
.bio-photo{left:189px;top:92px;width:188px;height:188px;border-radius:50%;background:radial-gradient(circle at 50% 45%,#c99d86 0%,#8c5f4b 45%,#2a1f1c 100%)}
.bio-title{left:405px;top:110px;font-family:"Mulish",sans-serif;font-size:24px;color:#555;letter-spacing:1px}
.bio-text{left:405px;top:147px;width:640px;font-size:13px;line-height:23px;color:#555}
.btn-outline{height:36px;border-radius:18px;border:1px solid var(--green);color:var(--green);font-size:12px;line-height:34px;text-align:center;text-transform:uppercase}
.bio .btn-outline{left:405px;top:225px;width:124px}

/* coaching */
.coaching{left:0;top:995px;width:1200px;height:443px;background:linear-gradient(100deg,var(--green-dark) 0%,#148a3e 40%,#2a9e4a 60%)}
.coaching-photo{left:0;top:0}
.coaching-title{left:132px;top:82px;font-family:"Mulish",sans-serif;font-size:34px;color:var(--white)}
.coaching-text{left:132px;top:140px;width:490px;font-size:14px;line-height:24px;color:var(--white)}
.coaching .btn-outline{left:132px;top:307px;width:130px;border-color:var(--white);color:var(--white)}

/* feature cards */
.card{top:1555px;width:462px;height:240px;background:var(--white)}
.card-book{left:109px;border:2px solid var(--purple)}
.card-speaking{left:591px;border:2px solid var(--green-bright)}
.card-icon{top:-66px;left:166px;width:130px;height:130px;border-radius:50%;background:var(--white)}
.card-kicker{top:72px;width:100%;text-align:center;font-family:"Mulish",sans-serif;font-size:19px;color:var(--purple)}
.card-title{top:100px;width:100%;text-align:center;font-family:"Mulish",sans-serif;font-size:24px;color:var(--purple)}
.card-speaking .card-title{top:80px;color:var(--green)}
.card-text{left:60px;width:342px;text-align:center;font-size:12.5px;line-height:23px;color:#888}
.card-book .card-text{top:138px}
.card-speaking .card-text{top:115px}
.card-btn{top:222px;left:141px}

/* blog */
.blog{left:0;top:1894px;width:1200px;height:500px;background:var(--light)}
.blog-heading{top:82px;width:1200px;text-align:center;font-family:"Mulish",sans-serif;font-size:30px;color:#333;letter-spacing:.5px}
.post{top:152px;width:470px;height:244px;background:var(--white);box-shadow:0 1px 4px rgba(0,0,0,.08)}
.post-image{left:0;top:0;width:212px;height:244px}
.post-body{left:232px;top:20px;width:222px}
.post-title{font-family:"Mulish",sans-serif;font-size:15px;line-height:20px;color:#333}
.post-date{margin-top:10px;font-size:12px;font-style:italic;color:var(--green);text-transform:uppercase}
.post-excerpt{margin-top:10px;font-size:11px;line-height:18.5px;color:#666}
.post-more{margin-top:8px;font-size:12px;color:#333}

/* newsletter */
.newsletter{left:0;top:2377px;width:1200px;height:366px;overflow:hidden}
.newsletter-bg{left:0;top:0;width:1200px;height:366px;background:linear-gradient(180deg,#8b82c8 0%,#a59ed8 55%,#b7b0e0 100%)}
.newsletter-wave{left:0;top:0}
.newsletter-title{top:82px;width:1200px;text-align:center;font-family:"Mulish",sans-serif;font-size:30px;line-height:36px;color:var(--white);text-transform:uppercase;letter-spacing:.5px}
.newsletter-sub{top:160px;width:1200px;text-align:center;font-family:"Mulish",sans-serif;font-size:18px;color:#f1efff}
.field{top:206px;height:43px;background:var(--white);font-size:15px;color:#999;line-height:43px;padding-left:16px}
.field-name{left:234px;width:273px}
.field-email{left:512px;width:276px}
.subscribe{left:795px;top:206px;width:146px;height:43px;border:2px solid var(--white);color:var(--white);font-size:15px;line-height:39px;text-align:center;text-transform:uppercase}

/* footer */
.site-footer{left:0;top:2743px;width:1200px;height:179px;background:var(--white)}
.badge{left:148px;top:35px;width:102px;height:102px;border-radius:50%;background:radial-gradient(circle,#e8e8e8 0%,#bcbcbc 70%,#9a9a9a 100%)}
.footer-nav{left:286px;top:55px;font-family:"Mulish",sans-serif;font-size:14px;color:#333;display:flex;gap:22px}
.copyright{left:288px;top:94px;font-size:12px;color:#aaa}
.social{top:56px;width:34px;height:34px;border:2px solid var(--green-bright)}
</style>
</head>
<body>

<header class="site-header abs">
  <div class="brand abs"><span class="brand-dot"></span><span class="brand-name">Clara Wendell</span></div>
  <nav class="main-nav abs">
    <a class="active" style="left:468px">Home</a>
    <a style="left:551px">Blog</a>
    <a style="left:619px">Store</a>
    <a style="left:697px">Speaking</a>
    <a style="left:808px">Coaching Program</a>
    <a style="left:1001px">Contact</a>
  </nav>
</header>

<section class="hero abs">
  <div class="hero-photo abs" role="img" aria-label="Beach at dusk with a young woman reading, seen from behind"></div>
  <svg class="arrow abs" style="left:72px" width="30" height="60" viewBox="0 0 30 60"><polyline points="26,4 4,30 26,56" fill="none" stroke="#fff" stroke-width="2"/></svg>
  <svg class="arrow abs" style="left:1100px" width="30" height="60" viewBox="0 0 30 60"><polyline points="4,4 26,30 4,56" fill="none" stroke="#fff" stroke-width="2"/></svg>
  <h1 class="hero-title abs">LAUNCHPAD FOR CAMPUS</h1>
  <p class="hero-sub abs">Steps and strategies to prepare you to<br>thrive in college and beyond</p>
  <div class="btn-solid abs">Read more</div>
  <div class="book abs" role="img" aria-label="Cover of the book Launchpad for Campus"></div>
  <svg class="hero-wave abs" width="1200" height="120" viewBox="0 0 1200 120" preserveAspectRatio="none"><path d="M0,40 C350,110 800,120 1200,10 L1200,120 L0,120 Z" fill="#efefef"/></svg>
</section>

<section class="bio abs">
  <div class="bio-photo abs" role="img" aria-label="Portrait of Clara Wendell"></div>
  <h2 class="bio-title abs">BIO</h2>
  <p class="bio-text abs">Clara Wendell is a certified teacher and holds advanced certification in academic coaching and tutoring. She also is a certified trainer in the Hollis Varga Growth Framework. She has three successful adult children, and helped them overcome learning differences and thrive.</p>
  <div class="btn-outline abs">Read more »</div>
</section>

<section class="coaching abs">
  <svg class="coaching-photo abs" width="1200" height="443" viewBox="0 0 1200 443" role="img" aria-label="Dandelion seed head against a green background">
    <defs><linearGradient id="dandelion" x1="0" y1="0" x2="1" y2="0"><stop offset="0" stop-color="#1d8f45"/><stop offset=".5" stop-color="#4cae55"/><stop offset="1" stop-color="#2a8a40"/></linearGradient></defs>
    <polygon points="720,0 1200,0 1200,443 540,443" fill="url(#dandelion)"/>
  </svg>
  <h2 class="coaching-title abs">Coaching Program</h2>
  <p class="coaching-text abs">Clara's approach is whole person oriented. Her programs help students learn life skills in addition to the study, time management skills, etc. offered by most academic coaching programs. Our program addresses all of the major causes of failure to graduate within 4 years, and is based on sound educational research. Clara's program initially provides the dailyinteraction needed to successfully change behaviors</p>
  <div class="btn-outline abs">Read more »</div>
</section>

<article class="card card-book abs">
  <div class="card-icon abs">
    <svg width="130" height="130" viewBox="0 0 130 130"><circle cx="65" cy="65" r="63" fill="#fff" stroke="#8a82c6" stroke-width="2"/><path d="M37,48 Q52,42 65,50 Q78,42 93,48 L93,84 Q78,78 65,86 Q52,78 37,84 Z M65,50 L65,86" fill="none" stroke="#8a82c6" stroke-width="2.5"/></svg>
  </div>
  <div class="card-kicker abs">My Book</div>
  <h3 class="card-title abs">Launchpad for Campus</h3>
  <p class="card-text abs">Steps and strategies to prepare you to thrive in college and beyond</p>
  <svg class="card-btn abs" width="180" height="40" viewBox="0 0 180 40"><polygon points="16,0 164,0 180,20 164,40 16,40 0,20" fill="#8a82c6"/><text x="90" y="25" text-anchor="middle" font-family="Mulish,sans-serif" font-size="15" fill="#fff">READ MORE</text></svg>
</article>

<article class="card card-speaking abs">
  <div class="card-icon abs">
    <svg width="130" height="130" viewBox="0 0 130 130"><circle cx="65" cy="65" r="63" fill="#fff" stroke="#3aa64f" stroke-width="2"/><path d="M40,56 L54,56 L84,40 L84,90 L54,74 L40,74 Z M50,74 L56,92 L64,92 L60,76 M90,56 L98,52 M90,65 L100,65 M90,74 L98,78" fill="none" stroke="#0f7d3f" stroke-width="2.5" stroke-linejoin="round"/></svg>
  </div>
  <h3 class="card-title abs">Speaking</h3>
  <p class="card-text abs">Praesent elementum elit at tellus nec ultricies sit amet porttitor mattis enim in massa libero interdum nec interdum vel blandit sed nulla in ullamcorper est eget tempor cursus neque mi</p>
  <svg class="card-btn abs" width="180" height="40" viewBox="0 0 180 40"><polygon points="16,0 164,0 180,20 164,40 16,40 0,20" fill="#3aa64f"/><text x="90" y="25" text-anchor="middle" font-family="Mulish,sans-serif" font-size="15" fill="#fff">READ MORE</text></svg>
</article>

<section class="blog abs">
  <h2 class="blog-heading abs">LATEST BLOG</h2>
  <article class="post abs" style="left:109px">
    <div class="post-image abs" role="img" aria-label="Two smiling students holding books" style="background:linear-gradient(135deg,#b08a6a,#6c5a4e 60%,#3f4a55)"></div>
    <div class="post-body abs">
      <h3 class="post-title">Sed ut perspiciatis unde omnis natus error sit voluptatem</h3>
      <p class="post-date">Sep 19, 2017</p>
      <p class="post-excerpt">Sed ut perspiciatis unde omnis iste natus voluptatem accusantium doloremque laudantium, totam rem aperiam, eaque ipsa quae ab illo inventore veritatis et quasi architecto beatae vitae dicta</p>
      <p class="post-more">Read More »</p>
    </div>
  </article>
  <article class="post abs" style="left:616px">
    <div class="post-image abs" role="img" aria-label="Student working on a laptop by a window" style="background:linear-gradient(135deg,#8a7a55,#4d5a48 55%,#2e4a6a)"></div>
    <div class="post-body abs">
      <h3 class="post-title">Sed ut perspiciatis unde omnis natus error sit voluptatem</h3>
      <p class="post-date">Sep 19, 2017</p>
      <p class="post-excerpt">Sed ut perspiciatis unde omnis iste natus voluptatem accusantium doloremque laudantium, totam rem aperiam, eaque ipsa quae ab illo inventore veritatis et quasi architecto beatae vitae dicta</p>
      <p class="post-more">Read More »</p>
    </div>
  </article>
</section>

<section class="newsletter abs">
  <div class="newsletter-bg abs" role="img" aria-label="Graduates jumping at sunset under a lavender tint"></div>
  <svg class="newsletter-wave abs" width="1200" height="60" viewBox="0 0 1200 60" preserveAspectRatio="none"><path d="M0,0 L1200,0 L1200,30 C850,0 400,0 0,40 Z" fill="#efefef"/></svg>
  <h2 class="newsletter-title abs">Sign up for our newsletter and<br>get the free report</h2>
  <p class="newsletter-sub abs">Seven Habits That Carry Your Teen Through University on Schedule and Budget</p>
  <div class="field field-name abs">Name</div>
  <div class="field field-email abs">Email address</div>
  <div class="subscribe abs">Subscribe</div>
</section>

<footer class="site-footer abs">
  <div class="badge abs" role="img" aria-label="Certified trainer seal"></div>
  <nav class="footer-nav abs"><span>Home</span><span>Blog</span><span>Store</span><span>Speaking</span><span>Coaching Program</span><span>Contact</span></nav>
  <p class="copyright abs">© 2017 Company Name &nbsp;All right reserved</p>
  <div class="social abs" style="left:923px"></div>
  <div class="social abs" style="left:963px"></div>
  <div class="social abs" style="left:1003px"></div>
  <div class="social abs" style="left:1043px"></div>
</footer>

</body>
</html>
```